Australia-Wide Industry Leader Bookkeeping Business Website Design Required

We need a website designed for our 10 year old bookkeeping business, Barwick & Lund. Barwick & Lund has been servicing the local & interstate communities of Australia, providing first-class BAS & Bookkeeping services with a personal touch unmatched by anyone else in the county.

What began 10 years ago as a small business focusing on family, friends and the local community, it has since grown into a well respected business with 95% of their business based solely on word of mouth and personal referrals from around Australia.

We would like to see designs that incorporate our existing brand/logo. The colours to be used on the website should be colours that work well with our logo. The design should communicate maturity, trust and confidence with a Web 2.0 look and feel.

We have produced mockups of the entire website as well as assets used in the mockups. Please reference the attached files. The mockups are an example of all the design elements that we want on each page. Designers are encouraged to use the mockups as a guideline only and for designers to use their own creativity.
Updates

This message is for new graphic designers who are considering commencing work on this project. Thank you for expressing an interest in our project. We would like to inform you that this project is close to completion as we have a number designs under very serious consideration.

We are currently in a position where we are disinterested providing feedback to improve on new designs submitted. We will provide feedback to improve new designs only if the submitted designs are very close to what we want for our website, and will only require 1 or 2 revision rounds to refine before the project completion date we will not work with designers to refine their newly submitted designs.

We feel that it is important for all designers to know the above information as we feel that your time and effort may be better spent working on another project.

Thank you for your understanding.

A big thank you for all the designs submitted. We are now in the process of selecting a design. Please be patient during this process. Thank you.

Target Market(s)

Busy Business Owners

Industry/Entity Type

Small Business

Requirements
Must have
• We require a rectangular "slide show" type feature to serve as a "teaser" to arouse the emotions of our website visitors. Each slide asks a specific question. The questions are:

- Is your paperwork in a mess?
- Do you need to get organised for the end of financial year?
- Are you sick & tired of endless amounts of paperwork & BASs?
- Do you feel frustrated & annoyed because you know your books need to be done?
- Do you lack the time & patience to get your paperwork done?
- Do you wish you had more time to do the things you enjoy doing?
- Contact Barwick & Lund today and we will transform your chaos into order.

Underneath the slide show will be a button to "Call Barwick & Lund Now - 03 5550 1827".

```html
<!DOCTYPE html>
<html lang="en">
<head>
<meta charset="utf-8">
<title>Barwick &amp; Lund – Services</title>
<link href="https://fonts.googleapis.com/css2?family=Tinos:wght@400;700&family=Arimo:wght@400;700&display=swap" rel="stylesheet">
<style>
  :root {
    --page: #ffffff;
    --frame: #c9ccd1;
    --ink: #1d1d1d;
    --muted: #8a8a8a;
    --heading: #b02a1c;
    --band: #cfd9e6;
    --band-edge: #7f99b8;
    --tick: #3f9a2e;
    --tick-dark: #2d7a1f;
    --map-sea: #eef1f5;
    --map-land: #c9ced6;
  }
  * { box-sizing: border-box; margin: 0; padding: 0; }
  html, body { width: 900px; height: 1200px; overflow: hidden; background: var(--page); }
  body {
    font-family: "Tinos", "Times New Roman", serif;
    color: var(--ink);
    font-size: 17px;
    line-height: 1.3;
  }
  .page {
    position: absolute; inset: 30px 24px;
    border: 2px solid var(--frame);
    padding: 30px 28px 0;
    overflow: hidden;
  }
  .row { display: flex; gap: 24px; }
  .col-main { width: 464px; flex: 0 0 464px; }
  .col-side { flex: 1; min-width: 0; }
  .section-title {
    font-family: "Arimo", Arial, sans-serif;
    font-size: 11px; font-weight: 700;
    color: var(--heading);
    text-transform: uppercase;
    white-space: nowrap;
    padding: 4px 8px 2px;
    background: linear-gradient(var(--page) 50%, var(--band) 50%);
    border-bottom: 3px solid var(--band-edge);
    margin-bottom: 16px;
  }
  .section-title.compact { font-size: 10px; letter-spacing: -0.1px; }
  .summary-grid {
    display: grid; grid-template-columns: 1fr 1fr;
    column-gap: 14px; row-gap: 12px;
  }
  .tick-item { display: flex; align-items: flex-start; gap: 8px; }
  .tick { flex: 0 0 22px; width: 22px; height: 22px; }
  .tick-list { display: flex; flex-direction: column; gap: 12px; }
  .referral { font-size: 15px; line-height: 1.3; margin-bottom: 12px; }
  .map {
    width: 100%; height: 260px;
    background: radial-gradient(ellipse at 55% 50%, var(--map-land) 0%, var(--map-land) 45%, var(--map-sea) 72%);
    border: 1px solid var(--frame);
  }
  .differences { margin-top: 40px; }
  .plain-text { margin-top: 12px; }
  .bullets { margin: 8px 0 0 40px; list-style: disc; }
  .bullets li { margin-bottom: 6px; }
  .quals-title { margin-top: 150px; }
  .callout {
    margin-top: 44px;
    border: 2px solid var(--ink);
    padding: 12px 10px 40px;
    text-align: center;
    font-family: "Arimo", Arial, sans-serif;
    font-weight: 700; font-size: 18px; line-height: 1.2;
  }
  .callout .faded { color: var(--muted); }
</style>
</head>
<body>
<svg width="0" height="0" style="position:absolute">
  <defs>
    <symbol id="tick-mark" viewBox="0 0 24 24">
      <circle cx="12" cy="12" r="11" fill="var(--tick)" stroke="var(--tick-dark)" stroke-width="1"/>
      <path d="M6.5 12.5l3.7 3.6 7.3-8" fill="none" stroke="#fff" stroke-width="2.6" stroke-linecap="round" stroke-linejoin="round"/>
    </symbol>
  </defs>
</svg>

<main class="page">
  <div class="row">
    <section class="col-main">
      <h2 class="section-title">To Summarize</h2>
      <div class="summary-grid">
        <div class="tick-item"><svg class="tick"><use href="#tick-mark"/></svg><span>Free Initial Consultation</span></div>
        <div class="tick-item"><svg class="tick"><use href="#tick-mark"/></svg><span>Superannuation &amp; Workcover</span></div>
        <div class="tick-item"><svg class="tick"><use href="#tick-mark"/></svg><span>Registered BAS Agent #90412-315</span></div>
        <div class="tick-item"><svg class="tick"><use href="#tick-mark"/></svg><span>Margin Scheme</span></div>
        <div class="tick-item"><svg class="tick"><use href="#tick-mark"/></svg><span>Bookkeeping</span></div>
        <div class="tick-item"><svg class="tick"><use href="#tick-mark"/></svg><span>Fuel Tax Credits</span></div>
        <div class="tick-item"><svg class="tick"><use href="#tick-mark"/></svg><span>BAS Preparation/ Lodgement</span></div>
        <div class="tick-item"><svg class="tick"><use href="#tick-mark"/></svg><span>Offsite &amp; onsite bookkeeping</span></div>
        <div class="tick-item"><svg class="tick"><use href="#tick-mark"/></svg><span>Payroll</span></div>
        <div class="tick-item"><svg class="tick"><use href="#tick-mark"/></svg><span>LedgerBooks Software &amp; Training</span></div>
        <div class="tick-item"><svg class="tick"><use href="#tick-mark"/></svg><span>IAS Preparation &amp; Lodgement</span></div>
        <div class="tick-item"><svg class="tick"><use href="#tick-mark"/></svg><span>Business Plans &amp; Budgets</span></div>
      </div>
    </section>
    <aside class="col-side">
      <p class="referral">95% of our clients come from client &amp; accountant referrals. We have clients all over Victoria, Queensland, NSW &amp; Western Australia, so no matter where you are, we can help.</p>
      <div class="map" role="img" aria-label="Map of Australia with pins marking client locations"></div>
    </aside>
  </div>

  <div class="row differences">
    <section class="col-main">
      <h2 class="section-title">What makes Barwick &amp; Lund different from other bookkeepers?</h2>
      <div class="tick-list">
        <div class="tick-item"><svg class="tick"><use href="#tick-mark"/></svg><span>We guarantee the quality of our work</span></div>
        <div class="tick-item"><svg class="tick"><use href="#tick-mark"/></svg><span>We have over 35 years of experience</span></div>
        <div class="tick-item"><svg class="tick"><use href="#tick-mark"/></svg><span>We have owned &amp; operated businesses 35 years</span></div>
        <div class="tick-item"><svg class="tick"><use href="#tick-mark"/></svg><span>The Barwick &amp; Lund Team are investors &amp; traders</span></div>
        <div class="tick-item"><svg class="tick"><use href="#tick-mark"/></svg><span>Extensive Business Network for your benefit</span></div>
        <div class="tick-item"><svg class="tick"><use href="#tick-mark"/></svg><span>Backed by a team of Accountants</span></div>
      </div>
      <p class="plain-text">We work with a team of elite accountants &amp; wealth creation professionals who coach us monthly in the following:</p>
      <ul class="bullets">
        <li>Asset Protection</li>
        <li>Superannuation &amp; Self Managed Superannuation Funds</li>
        <li>Property Investing</li>
      </ul>
      <p class="plain-text">Tax Strategies, tax structures &amp; best tax savings.</p>
      <p class="plain-text">We understand just how important it is to help lead &amp; guide our clients from making profits to:</p>
      <ul class="bullets">
        <li>Maximizing profits</li>
        <li>Wealth creation</li>
      </ul>
    </section>
    <aside class="col-side">
      <h2 class="section-title compact quals-title">Qualifications, memberships and partnerships</h2>
      <div class="tick-list">
        <div class="tick-item"><svg class="tick"><use href="#tick-mark"/></svg><span>Registered TaxCentral BAS Agent</span></div>
        <div class="tick-item"><svg class="tick"><use href="#tick-mark"/></svg><span>Certificate IV Financial Services</span></div>
        <div class="tick-item"><svg class="tick"><use href="#tick-mark"/></svg><span>Certificate III Financial Services</span></div>
        <div class="tick-item"><svg class="tick"><use href="#tick-mark"/></svg><span>Member of Guild of Certified Ledgerkeepers</span></div>
        <div class="tick-item"><svg class="tick"><use href="#tick-mark"/></svg><span>Platinum Member of Ledger Keepers Network</span></div>
        <div class="tick-item"><svg class="tick"><use href="#tick-mark"/></svg><span>Ledgerline Professional Partner</span></div>
        <div class="tick-item"><svg class="tick"><use href="#tick-mark"/></svg><span>TaxWise Partners</span></div>
      </div>
      <div class="callout">THIS IS SOMETHING<br><span class="faded">OTHER BOOKKEEPERS</span></div>
    </aside>
  </div>
</main>
</body>
</html>
```